Kestrel electrical letter head

Require a letter head to go with our new logo for our start up company. Something fresh and professional looking, also perhaps a "ghost"image of the logo in the centre of the page. Address to go on it PO Box 58, Kelsbrook 7386. Web address: www.kestrel-example.net.nz

```html
<!DOCTYPE html>
<html lang="en">
<head>
<meta charset="utf-8">
<title>Kestrel Electrical – Letterhead</title>
<link rel="stylesheet" href="https://fonts.googleapis.com/css2?family=Lexend:wght@600&display=swap">
<style>
  :root {
    --paper: #ffffff;
    --brand-blue: #2f6cc8;
    --brand-green: #9dcb3a;
    --ghost: #f2f2f2;
  }
  html, body {
    margin: 0;
    padding: 0;
    width: 933px;
    height: 1200px;
    overflow: hidden;
    background: var(--paper);
  }
  .letterhead {
    position: relative;
    width: 933px;
    height: 1200px;
    background: var(--paper);
    font-family: "Lexend", "Helvetica Neue", Arial, sans-serif;
    font-weight: 600;
    color: var(--brand-blue);
  }
  .brand {
    position: absolute;
    left: 40px;
    top: 62px;
    display: flex;
    align-items: center;
    gap: 10px;
  }
  .brand-dot {
    width: 30px;
    height: 30px;
    border-radius: 50%;
    background: var(--brand-green);
  }
  .brand-name {
    margin: 0;
    font-size: 23px;
    font-weight: 600;
    letter-spacing: 0.4px;
    text-transform: uppercase;
    line-height: 1;
    white-space: nowrap;
  }
  .contact {
    position: absolute;
    right: 42px;
    top: 76px;
    margin: 0;
    font-style: normal;
    font-size: 12px;
    line-height: 15px;
    text-transform: uppercase;
    white-space: nowrap;
  }
  .contact span { display: block; }
  .ghost-name {
    position: absolute;
    left: 0;
    top: 520px;
    width: 933px;
    text-align: center;
    font-size: 120px;
    line-height: 1;
    letter-spacing: 4px;
    text-transform: uppercase;
    color: var(--ghost);
    user-select: none;
  }
</style>
</head>
<body>
  <main class="letterhead">
    <header>
      <div class="brand">
        <span class="brand-dot" aria-hidden="true"></span>
        <h1 class="brand-name">Kestrel Electrical</h1>
      </div>
      <address class="contact">
        <span>0800 555 019</span>
        <span>www.kestrel-example.net.nz</span>
        <span>PO Box 58, Kelsbrook 7386</span>
      </address>
    </header>
    <div class="ghost-name" aria-hidden="true">Kestrel</div>
  </main>
</body>
</html>
```